Design eines Notizblocks für Holzverarbeitungsbetrieb
Zielgruppe
Wir sind ein Holzverarbeitungsbetrieb (Tischlerei / Zimmerei).
Wir haben einen Bodenständigen und gehobenen Kundenkreis.
Aufgabenstellung
das Design soll für einen Notizblock fein kariert sein.
Das Logo + Adresse + Telefonnummer + email (+ Dienstleistungen). Logofarbe ist Gelb-grün.
Adresse: Matthias Brandner Gasse 7, 5580 Tamsweg; Telefonnummer: +3916 8051 email: office@wendrasch.co.at
(Dienstleistungen: Zimmerei, Bautischler, Möbeltischler, Brandschutz, Fenster, Fassaden;)

```html
<!DOCTYPE html>
<html lang="de">
<head>
<meta charset="utf-8">
<title>Wendrasch Notizblock</title>
<link href="https://fonts.googleapis.com/css2?family=Montserrat:wght@500&family=Tinos&display=swap" rel="stylesheet">
<style>
  :root {
    --yellow: #f7d117;
    --olive: #3d4030;
    --grid: #c9c9c9;
    --paper: #ffffff;
    --backdrop: #e8e6e2;
    --ink: #1d1d1b;
  }
  * { margin: 0; padding: 0; box-sizing: border-box; }
  html, body { width: 1200px; height: 926px; overflow: hidden; }
  body { background: var(--backdrop); position: relative; font-family: "Tinos", serif; color: var(--ink); }

  .sheet { position: absolute; width: 510px; height: 721px; background: var(--paper); overflow: hidden; }
  .sheet--centered { left: 90px; top: 49px; }
  .sheet--corner { left: 637px; top: 133px; }

  .grid {
    position: absolute;
    background-color: var(--paper);
    background-image:
      linear-gradient(to right, var(--grid) 1px, transparent 1px),
      linear-gradient(to bottom, var(--grid) 1px, transparent 1px);
    background-size: 10px 10px;
    border-right: 1px solid var(--grid);
    border-bottom: 1px solid var(--grid);
  }
  .sheet--centered .grid { left: 30px; top: 31px; width: 451px; height: 645px; }
  .sheet--corner .grid { left: 2px; top: 13px; width: 496px; height: 658px; }

  .logo-field { position: absolute; background: var(--paper); display: flex; flex-direction: column; align-items: center; justify-content: center; gap: 10px; }
  .sheet--centered .logo-field { left: 189px; top: 31px; width: 132px; height: 85px; }
  .sheet--corner .logo-field { left: 357px; top: 13px; width: 142px; height: 116px; }
  .logo-square { width: 40px; height: 40px; border: 2px solid var(--olive); }
  .brand-name { font-family: "Montserrat", sans-serif; font-weight: 500; font-size: 14px; letter-spacing: 2px; color: var(--olive); }

  .stripe-band {
    position: absolute; left: 0; top: 0; width: 32px; height: 491px;
    background: linear-gradient(to bottom, var(--yellow) 0%, var(--yellow) 34%, var(--olive) 34%, var(--olive) 72%, var(--yellow) 72%, var(--yellow) 100%);
  }
  .sheet--corner .stripe-band { width: 30px; height: 486px; }

  .contact-row { position: absolute; left: 0; top: 0; width: 510px; font-size: 9.5px; line-height: 12px; }
  .contact { position: absolute; display: flex; align-items: flex-start; gap: 4px; white-space: nowrap; }
  .contact svg { width: 14px; height: 14px; flex: none; margin-top: -2px; }

  .services {
    position: absolute; right: 0; top: 699px; height: 21px; background: var(--yellow);
    font-size: 9.3px; white-space: nowrap;
    display: flex; align-items: center; justify-content: flex-end; padding-right: 34px;
  }
  .sheet--centered .services { width: 345px; }
  .sheet--corner .services { width: 362px; top: 698px; padding-right: 9px; font-size: 9.3px; }
</style>
</head>
<body>

<svg width="0" height="0" style="position:absolute">
  <defs>
    <symbol id="icon-pin" viewBox="0 0 14 14"><circle cx="7" cy="7" r="7" fill="#3d4030"/><path d="M7 3.2a2.3 2.3 0 0 0-2.3 2.3c0 1.7 2.3 4.6 2.3 4.6s2.3-2.9 2.3-4.6A2.3 2.3 0 0 0 7 3.2z" fill="#fff"/><circle cx="7" cy="5.5" r="0.8" fill="#3d4030"/></symbol>
    <symbol id="icon-phone" viewBox="0 0 14 14"><circle cx="7" cy="7" r="7" fill="#3d4030"/><rect x="4" y="3.5" width="6" height="7" rx="1.2" fill="#fff"/><path d="M5.3 5c.3 1.6 1.4 2.9 3 3.5l.6-.6" stroke="#3d4030" stroke-width="0.9" fill="none"/></symbol>
    <symbol id="icon-mail" viewBox="0 0 14 14"><circle cx="7" cy="7" r="7" fill="#3d4030"/><rect x="3.6" y="4.6" width="6.8" height="4.8" rx="0.6" fill="#fff"/><path d="M3.8 4.9 7 7.4l3.2-2.5" stroke="#3d4030" stroke-width="0.8" fill="none"/></symbol>
  </defs>
</svg>

<section class="sheet sheet--centered">
  <div class="grid"></div>
  <div class="logo-field">
    <div class="logo-square"></div>
    <div class="brand-name">WENDRASCH</div>
  </div>
  <div class="stripe-band" role="img" aria-label="Dekorative Holzmaserungs-Streifen in Gelb und Olivgrün"></div>
  <div class="contact-row" style="top:689px">
    <div class="contact" style="left:37px"><svg><use href="#icon-pin"/></svg><span>Adresse: Matthias Brandner Gasse 7,<br>5580 Tamsweg;</span></div>
    <div class="contact" style="left:206px"><svg><use href="#icon-phone"/></svg><span>Telefonnummer: +3916 8051</span></div>
    <div class="contact" style="left:357px"><svg><use href="#icon-mail"/></svg><span>email: office@wendrasch.co.at</span></div>
  </div>
  <div class="services">Zimmerei • Bautischler • Möbeltischler • Brandschutz • Fenster • Fassaden</div>
</section>

<section class="sheet sheet--corner">
  <div class="grid"></div>
  <div class="logo-field">
    <div class="logo-square"></div>
    <div class="brand-name">WENDRASCH</div>
  </div>
  <div class="stripe-band" role="img" aria-label="Dekorative Holzmaserungs-Streifen in Gelb und Olivgrün"></div>
  <div class="contact-row" style="top:686px">
    <div class="contact" style="left:28px"><svg><use href="#icon-pin"/></svg><span>Adresse: Matthias Brandner Gasse 7,<br>5580 Tamsweg;</span></div>
    <div class="contact" style="left:195px"><svg><use href="#icon-phone"/></svg><span>Telefonnummer: +3916 8051</span></div>
    <div class="contact" style="left:349px"><svg><use href="#icon-mail"/></svg><span>email: office@wendrasch.co.at</span></div>
  </div>
  <div class="services">Zimmerei ● Bautischler ● Möbeltischler ● Brandschutz ● Fenster ● Fassaden</div>
</section>

</body>
</html>
```